quiet meadow therapy (QMT)

I need to build a website for my therapy business.
There are two parts to the website
on the landing page; they choose whether they are therapists making a referral or patients needing more information.
After that, they are taken to their respective pages.
There is the textual information and a referral form on the therapist page, and on the patient page, the text is a bit different, and there will be a booking page on the patient page.
Visually minimal, it's a therapeutic website. I want it clean, clinical, and modern
colors: greenish blue or maybe orangish
PHP/html code
Updates

Hi everyone
I'm very sorry for the lack of responses to your designs. I am trying to work it out, but this platform has been a challenge for me.
I appreciate everyone's efforts, and I am unsure how to rate designs and move forward with the ones I like. There is a 5-star rating, but I don't understand how I'm supposed to politely say that it is not it without feeling like I'm going to affect someone's future rating negatively.
Please understand me. Thank you

Designs look the same

Target Market(s)

therapy and stress management

Industry/Entity Type

stress management therapy

Coding

Coded - Design and coding required

Number of Pages Required

5+ page

Font styles to use
Serif

Colors
0094D4
00A9DD
6FCCEA
C7EBF8
E9F6FB
00AB8E
00BBA5
67D7C9
C6EFE9
E9F9F6

Requirements
Must have
• landing page that that have 2 options. one for therapist another for patient

```html
<!DOCTYPE html>
<html lang="en">
<head>
<meta charset="utf-8">
<title>Quiet Meadow Therapy</title>
<link href="https://fonts.googleapis.com/css2?family=Raleway:wght@500;600;700&family=Poppins:ital,wght@0,400;0,500;0,600;1,400&display=swap" rel="stylesheet">
<style>
:root{
  --teal:#17a084;
  --orange:#f7921e;
  --ink:#1d1d1d;
  --muted:#6b6b6b;
  --stage:#e6e6e6;
  --panel:#e9e9e9;
  --white:#ffffff;
}
*{box-sizing:border-box;margin:0;padding:0}
html,body{width:1200px;height:3836px;overflow:hidden}
body{background:var(--stage);font-family:'Poppins',sans-serif;color:var(--ink);position:relative}
.abs{position:absolute}
.heading{font-family:'Raleway',sans-serif;font-weight:700}

/* landing screen */
.landing{left:240px;top:110px;width:720px;height:445px;overflow:hidden;border-radius:6px;
  background:linear-gradient(135deg,#2c2a28,#111 55%,#242220)}
.landing-brand{left:0;width:100%;top:62px;text-align:center;color:var(--white)}
.landing-brand .name{font-family:'Raleway',sans-serif;font-weight:600;font-size:48px;line-height:56px}
.landing-brand .tag{font-family:'Raleway',sans-serif;font-size:11px;letter-spacing:1px;color:var(--orange);font-weight:600;margin-top:6px}
.choice{width:134px;text-align:center;color:var(--white);top:195px}
.choice .disc{width:134px;height:134px;border-radius:50%;border:3px solid rgba(255,255,255,.85);display:flex;align-items:center;justify-content:center;font-size:10px;font-weight:600}
.choice .disc.therapist{background:radial-gradient(circle,#f6a623,#d98200)}
.choice .disc.patient{background:linear-gradient(135deg,#d4d2d0,#7a7672)}
.choice .label{font-family:'Raleway',sans-serif;font-weight:700;font-size:19px;margin-top:16px;white-space:nowrap}

/* website */
.page{left:213px;top:774px;width:774px;height:2975px;background:var(--white);overflow:hidden}
.topbar{left:0;top:0;width:100%;height:27px;background:var(--teal);color:var(--white);font-size:9px;display:flex;justify-content:flex-end;align-items:center;gap:18px;padding-right:72px}
.nav{left:0;top:27px;width:100%;height:47px;display:flex;align-items:center;padding:0 72px;border-bottom:1px solid #eee}
.nav .logo{font-family:'Raleway',sans-serif;font-weight:700;font-size:21px;color:var(--ink)}
.nav ul{list-style:none;display:flex;gap:22px;margin-left:46px;font-size:10px;color:#444}
.nav ul li.active{color:var(--orange)}
.btn{background:var(--orange);color:var(--white);font-size:9px;font-weight:500;display:flex;align-items:center;justify-content:center;border-radius:3px}
.nav .btn{margin-left:auto;width:114px;height:28px}

.hero{left:0;top:74px;width:100%;height:426px;background:linear-gradient(100deg,#3f3d3b,#67625d 45%,#857e76 70%,#4b4946)}
.hero-title{left:71px;top:125px;color:var(--white);font-size:38px;font-family:'Raleway',sans-serif;font-weight:700}
.hero-copy{left:73px;top:172px;width:260px;color:#eee;font-size:8.5px;line-height:18px}
.hero .btn-teal{left:71px;top:252px;width:114px;height:32px;background:var(--teal);color:#fff;font-size:10px;border-radius:3px;display:flex;align-items:center;justify-content:center}
.arrow{color:#fff;font-size:26px;line-height:1}
.dots{display:flex;gap:4px}
.dots span{width:7px;height:7px;border-radius:50%;border:1px solid #999;background:#fff}
.dots span.on{border-color:var(--orange);background:var(--orange)}

.section-title{left:0;width:100%;text-align:center;font-size:28px}
.rule{width:56px;height:3px;background:var(--orange)}
.card-title{font-size:11px;font-weight:600}
.card-text{font-size:8px;line-height:15px;color:var(--muted)}
.more{font-size:8.5px;color:var(--teal);font-weight:500}

.about{left:0;top:987px;width:100%;height:333px;background:var(--panel)}
.about-copy{left:431px;top:98px;width:292px;font-size:7.5px;line-height:16.5px;color:var(--muted)}
.about-copy p+p{margin-top:10px}

.quotes{left:0;top:1780px;width:100%;height:440px}
.testimonial{width:167px;height:219px;background:rgba(255,255,255,.12);color:#fff;padding:16px 14px;font-size:7.5px;font-style:italic;line-height:14.5px}
.testimonial .who{position:absolute;left:14px;bottom:14px;display:flex;align-items:center;gap:10px;font-style:normal}
.testimonial .who i{width:36px;height:36px;border-radius:50%;background:linear-gradient(135deg,#e0c5b2,#a8806a)}
.testimonial .who b{font-weight:500;font-size:9px;display:block}
.testimonial .who small{color:#fff;font-size:8px;letter-spacing:1px}
.testimonial .divider{position:absolute;left:0;right:0;bottom:62px;height:1px;background:rgba(255,255,255,.5)}

.field{border:1px solid #bdbdbd;font-size:9px;color:#444;padding:0 10px;display:flex;align-items:center}
.field.tall{align-items:flex-start;padding-top:12px}
.submit{left:295px;top:2545px;width:183px;height:33px;background:var(--teal);color:#fff;font-size:11px;font-weight:600;letter-spacing:1px;display:flex;align-items:center;justify-content:center}

.footer-nav{left:0;width:100%;top:2685px;display:flex;justify-content:center;gap:22px;color:#ddd;font-size:10px}
.hline{left:70px;width:631px;height:1px;background:#555}
.info-box{width:205px;height:82px;border:1px solid #777;color:#eee;font-size:8.5px;line-height:17px;text-align:center;padding-top:32px}
.info-icon{width:83px;height:57px;background:var(--orange);display:flex;align-items:center;justify-content:center}
</style>
</head>
<body>

<section class="abs landing" aria-label="Landing page">
  <div class="abs" role="img" aria-label="Dim background photo of a group therapy session" style="inset:0;background:radial-gradient(ellipse at 70% 40%,rgba(90,80,70,.4),transparent 60%)"></div>
  <div class="abs landing-brand">
    <div class="name">QMT</div>
    <div class="tag">QUIET MEADOW THERAPY</div>
  </div>
  <a class="abs choice" style="left:197px">
    <div class="disc therapist" role="img" aria-label="Photo of a therapist with orange overlay">GO TO LINK</div>
    <div class="label">THERAPISTS</div>
  </a>
  <a class="abs choice" style="left:363px">
    <div class="disc patient" role="img" aria-label="Photo of a patient reading"></div>
    <div class="label">PATIENTS</div>
  </a>
</section>

<main class="abs page">
  <div class="abs topbar"><span>&#9990; Call Now - +1 555 014 2290</span><span>&#9993; Email - hello@quietmeadowtherapy.com</span></div>
  <header class="abs nav">
    <div class="logo">QMT</div>
    <ul><li class="active">Home</li><li>About Us</li><li>Services</li><li>Blog</li><li>Testimonials</li><li>Contact</li></ul>
    <div class="btn">Book a Appointment</div>
  </header>

  <section class="abs hero" role="img" aria-label="Photo of a therapist listening to a client">
    <h1 class="abs hero-title">QMT</h1>
    <p class="abs hero-copy">Lorem ipsum dolor sit amet, consectetur adipiscing elit, sed do eiusmod tempor incididunt ut labore et dolore magna aliqua. Ut enim ad minim veniam, quis nostrud exercitation ullamco laboris nisi ut aliquip ex ea commodo consequat.</p>
    <div class="abs btn-teal">Get Started</div>
    <div class="abs arrow" style="left:26px;top:195px">&#8249;</div>
    <div class="abs arrow" style="right:26px;top:195px">&#8250;</div>
    <div class="abs dots" style="left:364px;top:360px"><span class="on"></span><span></span><span></span><span></span><span></span></div>
  </section>
  <svg class="abs" style="left:0;top:420px" width="774" height="90" viewBox="0 0 774 90">
    <polygon points="0,58 774,0 774,22 0,80" fill="#f7921e"/>
    <polygon points="0,80 774,20 774,90 0,90" fill="#ffffff"/>
  </svg>

  <h2 class="abs section-title heading" style="top:538px">Our Services</h2>
  <div class="abs rule" style="left:359px;top:583px"></div>
  <article class="abs" style="left:71px;top:610px;width:204px">
    <div role="img" aria-label="Photo of a couple in a therapy session" style="height:176px;background:linear-gradient(135deg,#cbc5bd,#726a63)"></div>
    <h3 class="card-title" style="margin-top:14px">Couples Therapy</h3>
    <p class="card-text" style="margin-top:6px">Lorem ipsum dolor sit amet, consectetur adipiscing elit, sed do eiusmod tempor incididunt ut labore et dolore magna aliqua.</p>
    <p class="more" style="margin-top:6px">Read More &#10230;</p>
  </article>
  <article class="abs" style="left:284px;top:610px;width:204px">
    <div role="img" aria-label="Photo of a woman talking about depression" style="height:176px;background:linear-gradient(135deg,#dad5cd,#7d726c)"></div>
    <h3 class="card-title" style="margin-top:14px">Depression Problem</h3>
    <p class="card-text" style="margin-top:6px">Lorem ipsum dolor sit amet, consectetur adipiscing elit, sed do eiusmod tempor incididunt ut labore et dolore magna aliqua.</p>
    <p class="more" style="margin-top:6px">Read More &#10230;</p>
  </article>
  <article class="abs" style="left:497px;top:610px;width:204px">
    <div role="img" aria-label="Photo of a counsellor with a child" style="height:176px;background:linear-gradient(135deg,#e7dfd3,#ab9c88)"></div>
    <h3 class="card-title" style="margin-top:14px">Children Counselling</h3>
    <p class="card-text" style="margin-top:6px">Lorem ipsum dolor sit amet, consectetur adipiscing elit, sed do eiusmod tempor incididunt ut labore et dolore magna aliqua.</p>
    <p class="more" style="margin-top:6px">Read More &#10230;</p>
  </article>
  <div class="abs dots" style="left:364px;top:921px"><span class="on"></span><span></span><span></span><span></span><span></span></div>

  <section class="abs about">
    <div class="abs" role="img" aria-label="Photo of a smiling therapist in front of a group session" style="left:0;top:0;width:410px;height:333px;background:linear-gradient(90deg,#2e2d2c,#4a4541 55%,#cfc8bd)"></div>
    <h2 class="abs heading" style="left:431px;top:40px;font-size:26px">About Us</h2>
    <div class="abs rule" style="left:431px;top:78px"></div>
    <div class="abs about-copy">
      <p>Lorem ipsum dolor sit amet, consectetur adipiscing elit, sed do incididunt ut labore et dolore magna aliqua. Ut enim ad minim veniam, exercitation ullamco laboris nisi ut aliquip ex ea commodo consequat. Duis aute reprehenderit in voluptate velit esse cillum dolore eu fugiat nulla pariatur. occaecat cupidatat non proident, sunt in culpa qui officia deserunt mollit anim id est laborum</p>
      <p>Lorem ipsum dolor sit amet, consectetur adipiscing elit, sed do incididunt ut labore et dolore magna aliqua. Ut enim ad minim veniam, exercitation ullamco laboris nisi ut aliquip ex ea commodo consequat.</p>
    </div>
    <div class="abs btn" style="left:431px;top:258px;width:114px;height:32px;font-size:10px;box-shadow:0 3px 6px rgba(0,0,0,.2)">Read More</div>
  </section>

  <h2 class="abs section-title heading" style="top:1374px">The Latest News</h2>
  <p class="abs" style="left:180px;top:1412px;width:414px;text-align:center;font-size:9px;line-height:19px;color:#555">Lorem ipsum dolor sit amet, consectetur adipiscing elit, sed do eiusmod tempor incididunt ut labore et dolore magna aliqua</p>
  <div class="abs rule" style="left:345px;top:1458px;width:84px;height:2px"></div>
  <div class="abs arrow" style="left:60px;top:1558px;color:#333;font-size:24px">&#8249;</div>
  <div class="abs arrow" style="left:702px;top:1558px;color:#333;font-size:24px">&#8250;</div>
  <article class="abs" style="left:92px;top:1485px;width:183px">
    <div role="img" aria-label="Photo of a counselling session" style="height:172px;border-radius:0 22px 0 0;background:linear-gradient(135deg,#d0c7b9,#605b54);box-shadow:3px 3px 6px rgba(0,0,0,.2)"></div>
    <p style="font-size:7px;margin-top:12px"><span style="color:var(--orange)">&#9638;</span> July 25-2022</p>
    <h3 style="font-size:8px;font-weight:600;margin-top:6px">Lorem ipsum dolor sit amet, adipiscing</h3>
    <p class="card-text" style="font-size:7px;line-height:14px;margin-top:2px">Lorem ipsum dolor sit consectetur<br>adipiscing elit, sed do</p>
    <p class="more" style="text-decoration:underline;font-size:8px;margin-top:4px">Read More</p>
  </article>
  <article class="abs" style="left:296px;top:1485px;width:183px">
    <div role="img" aria-label="Photo of a bright therapy room" style="height:172px;border-radius:0 22px 0 0;background:linear-gradient(135deg,#e5e3df,#7e7a75);box-shadow:3px 3px 6px rgba(0,0,0,.2)"></div>
    <p style="font-size:7px;margin-top:12px"><span style="color:var(--orange)">&#9638;</span> July 25-2022</p>
    <h3 style="font-size:8px;font-weight:600;margin-top:6px">Lorem ipsum dolor sit amet, adipiscing</h3>
    <p class="card-text" style="font-size:7px;line-height:14px;margin-top:2px">Lorem ipsum dolor sit consectetur<br>adipiscing elit, sed do</p>
    <p class="more" style="text-decoration:underline;font-size:8px;margin-top:4px">Read More</p>
  </article>
  <article class="abs" style="left:499px;top:1485px;width:183px">
    <div role="img" aria-label="Photo of a therapist taking notes" style="height:172px;border-radius:0 22px 0 0;background:linear-gradient(135deg,#7e6c57,#324048);box-shadow:3px 3px 6px rgba(0,0,0,.2)"></div>
    <p style="font-size:7px;margin-top:12px"><span style="color:var(--orange)">&#9638;</span> July 25-2022</p>
    <h3 style="font-size:8px;font-weight:600;margin-top:6px">Lorem ipsum dolor sit amet, adipiscing</h3>
    <p class="card-text" style="font-size:7px;line-height:14px;margin-top:2px">Lorem ipsum dolor sit consectetur<br>adipiscing elit, sed do</p>
    <p class="more" style="text-decoration:underline;font-size:8px;margin-top:4px">Read More</p>
  </article>

  <section class="abs quotes">
    <svg class="abs" style="left:0;top:0" width="774" height="440" viewBox="0 0 774 440">
      <polygon points="428,36 774,0 774,30" fill="#f7921e"/>
      <polygon points="0,93 774,26 774,355 0,423" fill="#17a084"/>
      <polygon points="283,423 774,365 774,345 310,398" fill="#f7921e"/>
    </svg>
    <h2 class="abs heading" style="left:71px;top:153px;font-size:27px;line-height:30px;color:#fff;font-weight:600">What Our Clients<br>Says</h2>
    <div class="abs rule" style="left:71px;top:220px;width:40px;height:2px"></div>
    <p class="abs" style="left:71px;top:234px;width:260px;font-size:8px;line-height:16px;color:#fff">Lorem ipsum dolor sit amet, consectetur adipiscing elit, sed do eiusmod tempor incididunt ut labore et dolore magna aliqua. Ut enim ad minim veniam, quis nostrud exercitation</p>
    <div class="abs" style="left:71px;top:296px;display:flex;gap:4px">
      <span style="width:17px;height:17px;border-radius:50%;background:#fff;color:var(--teal);font-size:10px;display:flex;align-items:center;justify-content:center">&#8592;</span>
      <span style="width:17px;height:17px;border-radius:50%;background:#fff;color:var(--teal);font-size:10px;display:flex;align-items:center;justify-content:center">&#8594;</span>
    </div>
    <div class="abs testimonial" style="left:360px;top:113px">
      Lorem ipsum dolor sit consectetur adipiscing elit, sed incididunt ut labore et dolore magna aliqua. Ut enim ad minim veniam, quis nostrud exercitation ullamco laboris nisi ut aliquip ex ea commodo consequat. Duis aute irure dolor in reprehendrit in voluptate velit esse cillum dolore
      <div class="divider"></div>
      <div class="who"><i role="img" aria-label="Client portrait"></i><div><b>Dana Whitlow</b><small>&#9733;&#9733;&#9733;&#9733;&#9733;</small></div></div>
    </div>
    <div class="abs testimonial" style="left:535px;top:113px">
      Lorem ipsum dolor sit consectetur adipiscing elit, sed incididunt ut labore et dolore magna aliqua. Ut enim ad minim veniam, quis nostrud exercitation ullamco laboris nisi ut aliquip ex ea commodo consequat. Duis aute irure dolor in reprehendrit in voluptate velit esse cillum dolore
      <div class="divider"></div>
      <div class="who"><i role="img" aria-label="Client portrait"></i><div><b>Dana Whitlow</b><small>&#9733;&#9733;&#9733;&#9733;&#9733;</small></div></div>
    </div>
  </section>

  <h2 class="abs section-title heading" style="top:2247px">Contact Us</h2>
  <div class="abs rule" style="left:359px;top:2292px"></div>
  <div class="abs field" style="left:136px;top:2320px;width:246px;height:35px">First Name</div>
  <div class="abs field" style="left:389px;top:2320px;width:247px;height:35px">Last Name</div>
  <div class="abs field" style="left:136px;top:2369px;width:500px;height:34px">Email Address</div>
  <div class="abs field" style="left:136px;top:2415px;width:500px;height:34px">Subject</div>
  <div class="abs field tall" style="left:136px;top:2461px;width:500px;height:70px">Message</div>
  <div class="abs submit">SUBMIT</div>

  <svg class="abs" style="left:0;top:2600px" width="774" height="375" viewBox="0 0 774 375">
    <polygon points="0,6 774,30 774,375 0,375" fill="#161616"/>
    <polygon points="0,0 774,34 774,46 0,6" fill="#f7921e"/>
    <polygon points="0,0 774,0 774,34" fill="#ffffff"/>
  </svg>
  <div class="abs" role="img" aria-label="Dim background photo" style="left:0;top:2650px;width:774px;height:325px;background:radial-gradient(ellipse at 60% 30%,rgba(70,60,50,.35),transparent 70%)"></div>
  <nav class="abs footer-nav"><span>Home</span><span>About Us</span><span>Services</span><span>Blog</span><span>Testimonials</span><span>Contact</span></nav>
  <div class="abs hline" style="top:2734px"></div>

  <div class="abs info-box" style="left:70px;top:2792px">Lorem ipsum dolor sit amet, consectetur<br>adipiscing elit, sed</div>
  <div class="abs info-icon" style="left:131px;top:2762px">
    <svg width="16" height="20" viewBox="0 0 16 20"><path d="M8 0C3.6 0 0 3.5 0 7.8 0 13.5 8 20 8 20s8-6.5 8-12.2C16 3.5 12.4 0 8 0zm0 11a3.2 3.2 0 1 1 0-6.4A3.2 3.2 0 0 1 8 11z" fill="#fff"/></svg>
  </div>
  <div class="abs info-box" style="left:283px;top:2792px">Telephone:<br>+1 555 014 2290</div>
  <div class="abs info-icon" style="left:344px;top:2762px">
    <svg width="18" height="18" viewBox="0 0 24 24"><path d="M6.6 10.8a15.2 15.2 0 0 0 6.6 6.6l2.2-2.2c.3-.3.7-.4 1-.2 1.1.4 2.3.6 3.6.6.6 0 1 .4 1 1V20c0 .6-.4 1-1 1A17 17 0 0 1 3 4c0-.6.4-1 1-1h3.5c.6 0 1 .4 1 1 0 1.3.2 2.5.6 3.6.1.3 0 .7-.2 1z" fill="#fff"/></svg>
  </div>
  <div class="abs info-box" style="left:496px;top:2792px">Email:<br>hello@quietmeadowtherapy.com</div>
  <div class="abs info-icon" style="left:557px;top:2762px">
    <svg width="18" height="14" viewBox="0 0 18 14"><rect x="0" y="0" width="18" height="14" rx="1" fill="#fff"/><path d="M1 1l8 6 8-6" stroke="#f7921e" stroke-width="1.6" fill="none"/></svg>
  </div>

  <div class="abs hline" style="top:2911px"></div>
  <p class="abs" style="left:0;width:100%;top:2938px;text-align:center;font-size:8px;color:#ddd">&copy; 2022 All Rights Reserved</p>
  <span class="abs" style="left:689px;top:2937px;width:12px;height:12px;border:1.5px solid #ddd;border-radius:3px"></span>
</main>

</body>
</html>
```